Business card design for new brand

We have recently rebranded and need a new business card template.

We are an insurance underwriting agency. All of our products are sold via other partner companies, so these are just to pass on our details to other organisations.

We would like to see designs that use the colour green (current stationary generally uses lime green (rgb 142,190,63) and forest green (0,154,79) to comply with our logo's colours. We are happy with other shades of green.

Business cards need to include our logo, as well as space for:
1. Full name
2. Qualifications (optional)
3. Title
4. Office number
5. Mobile number
6. Email address

Our logo is enclosed here.

```html
<!DOCTYPE html>
<html lang="en">
<head>
<meta charset="utf-8">
<title>Northvale Cover – Business Card</title>
<link href="https://fonts.googleapis.com/css2?family=Arimo:wght@400;700&display=swap" rel="stylesheet">
<style>
  :root {
    --page-bg: #e9e9e8;
    --card-white: #fbfbfb;
    --ink: #1c1c1c;
    --forest: #009a4f;
    --name-green: #1f8a3c;
    --lime: #8ebe3f;
    --deep-green: #0e4f28;
    --mid-green: #17693a;
    --rule: #3a3a3a;
  }
  * { box-sizing: border-box; margin: 0; padding: 0; }
  html, body { width: 1200px; height: 801px; overflow: hidden; }
  body {
    background: var(--page-bg);
    font-family: "Arimo", Arial, sans-serif;
    color: var(--ink);
    position: relative;
  }
  .card {
    position: absolute;
    top: 236px;
    width: 530px;
    height: 303px;
    border-radius: 3px;
    box-shadow: 0 10px 28px rgba(0,0,0,.18);
    overflow: hidden;
  }
  .card--front {
    left: 50px;
    background: var(--card-white);
    border-bottom: 4px solid var(--forest);
  }
  .card--back {
    left: 620px;
    background: linear-gradient(135deg, var(--deep-green) 0%, var(--mid-green) 55%, #135c31 100%);
  }
  .brand {
    position: absolute;
    display: flex;
    align-items: center;
    gap: 12px;
    font-weight: 700;
    line-height: 1.05;
  }
  .card--front .brand { left: 34px; top: 126px; width: 210px; color: var(--ink); }
  .brand__square {
    width: 30px; height: 30px;
    background: var(--lime);
    flex: none;
  }
  .brand__name { font-size: 30px; letter-spacing: .5px; white-space: nowrap; }
  .brand__sub { display: block; font-size: 15px; letter-spacing: 1px; margin-top: 4px; }
  .divider {
    position: absolute;
    left: 262px; top: 40px;
    width: 1px; height: 222px;
    background: var(--rule);
  }
  .contact {
    position: absolute;
    left: 284px; top: 46px;
    font-size: 13.5px;
    line-height: 1.35;
  }
  .contact__name { color: var(--name-green); font-size: 20px; font-weight: 700; }
  .contact__title { font-size: 13.5px; margin-bottom: 14px; }
  .contact__address { margin-bottom: 14px; }
  .contact__list { list-style: none; }
  .contact__list li { display: flex; align-items: center; gap: 8px; height: 19px; }
  .contact__list svg { width: 12px; height: 12px; flex: none; }
  .card--back .brand {
    left: 0; right: 0; top: 104px;
    justify-content: center;
    color: #ffffff;
  }
  .card--back .brand__name { font-size: 46px; }
  .card--back .brand__sub { font-size: 22px; }
</style>
</head>
<body>
  <section class="card card--front" aria-label="Business card front">
    <div class="brand">
      <span class="brand__square"></span>
      <span class="brand__name">Northvale<span class="brand__sub">Cover Pty Ltd</span></span>
    </div>
    <div class="divider"></div>
    <div class="contact">
      <p class="contact__name">Daniel Carter</p>
      <p class="contact__title">Manager</p>
      <p class="contact__address">Your address, city<br>state, ZIP 0000</p>
      <ul class="contact__list">
        <li><svg viewBox="0 0 12 12"><path d="M2.5 1l2 2.2-1 1.3a6 6 0 0 0 4 4l1.3-1 2.2 2-1.2 1.5C5 10.8 1.2 7 .9 2.2z" fill="var(--forest)"/></svg>123-456-2100</li>
        <li><svg viewBox="0 0 12 12"><rect x="3" y=".8" width="6" height="10.4" rx="1" fill="none" stroke="var(--forest)" stroke-width="1.3"/></svg>123-456-2100</li>
        <li><svg viewBox="0 0 12 12"><rect x=".8" y="2.3" width="10.4" height="7.4" fill="none" stroke="var(--forest)" stroke-width="1.2"/><path d="M1 2.6l5 4 5-4" fill="none" stroke="var(--forest)" stroke-width="1.2"/></svg>name@northvale.example</li>
        <li><svg viewBox="0 0 12 12"><circle cx="6" cy="6" r="5.2" fill="var(--forest)"/><path d="M1 6h10M6 .8v10.4M2 3.5h8M2 8.5h8" stroke="#fff" stroke-width=".7"/></svg>www.northvale.example</li>
      </ul>
    </div>
  </section>

  <section class="card card--back" aria-label="Business card back">
    <div class="brand">
      <span class="brand__name">Northvale<span class="brand__sub">Cover Pty Ltd</span></span>
    </div>
  </section>
</body>
</html>
```